DOVVRANTI Label and bottle design

We have already provided attached an idea concept of a label and bottle shape example, we now require designers to take this basic concept and advance it to the final label design using your own design creativity.
Please see attached the full product brief

```html
<!DOCTYPE html>
<html lang="en">
<head>
<meta charset="utf-8">
<title>DOVVRANTI – INK PURGE label</title>
<link href="https://fonts.googleapis.com/css2?family=Montserrat:ital,wght@0,400;0,500;0,600;0,700;0,800;0,900;1,800;1,900&display=swap" rel="stylesheet">
<style>
  :root{
    --yellow:#f4ea2a;
    --black:#0d0d0d;
    --charcoal:#1c1c1c;
    --white:#ffffff;
    --red:#e3161b;
    --blue:#1d9bd9;
    --green:#23a64a;
    --amber:#f2b705;
    --page:#ffffff;
  }
  *{box-sizing:border-box;margin:0;padding:0}
  html,body{width:1200px;height:750px;overflow:hidden;background:var(--page)}
  body{font-family:"Montserrat",sans-serif;position:relative}
  .label{position:absolute;left:132px;top:7px;width:935px;height:735px}
  .panel{position:absolute;top:0;height:735px;overflow:hidden}

  /* front */
  .front{left:0;width:467px;background:var(--black)}
  .front-texture{position:absolute;left:0;top:26px;width:467px;height:694px;
    background:radial-gradient(ellipse at 50% 45%,#2a2a2a 0%,#141414 60%,#0a0a0a 100%)}
  .front .top-strip{position:absolute;left:0;top:0;width:467px;height:26px;background:var(--yellow)}
  .tab{position:absolute;top:0;height:45px;border-radius:0 0 22px 22px;
    display:flex;align-items:center;justify-content:center;
    font-weight:800;font-size:18.5px;letter-spacing:.3px}
  .front .tab{left:108px;width:250px;background:var(--yellow);color:var(--black)}
  .brand{position:absolute;left:20px;width:427px;top:170px;text-align:center}
  .brand-name{font-weight:900;font-size:56px;color:var(--yellow);letter-spacing:1px;line-height:1}
  .brand-tagline{margin-top:12px;font-weight:700;font-size:10.5px;color:var(--white);letter-spacing:.4px}
  .product-name{position:absolute;left:0;width:467px;top:358px;text-align:center;
    font-weight:900;font-style:italic;font-size:44px;color:var(--yellow);line-height:1}
  .product-sub{position:absolute;left:95px;width:277px;top:404px;height:24px;background:var(--yellow);
    color:var(--black);font-weight:900;font-style:italic;font-size:14.5px;
    display:flex;align-items:center;justify-content:center}
  .claims{position:absolute;left:53px;top:462px;display:flex;gap:21px}
  .claim{width:74px;text-align:center;color:var(--white);font-weight:800;font-size:11px;line-height:14.5px}
  .claim svg{display:block;margin:0 auto 9px}
  .suitable{position:absolute;left:150px;top:642px;width:92px;text-align:right;
    font-weight:800;font-size:13px;line-height:17px;color:var(--white)}
  .suitable span{color:var(--yellow)}
  .ink-badges{position:absolute;left:256px;top:639px;display:flex;gap:9px}
  .ink-badge{width:55px;height:55px;border-radius:6px;border:2px solid #fff;position:relative;
    display:flex;flex-direction:column;align-items:center;justify-content:flex-end;padding-bottom:8px}
  .ink-badge.blue{background:var(--blue)}
  .ink-badge.green{background:var(--green)}
  .ink-badge.amber{background:var(--amber)}
  .ink-badge svg{position:absolute;top:7px;left:50%;transform:translateX(-50%)}
  .ink-badge em{font-style:normal;font-weight:700;font-size:4.5px;color:#fff}
  .weight{position:absolute;left:0;top:660px;width:74px;height:62px;background:var(--yellow);
    border-radius:0 30px 0 0;font-weight:900;color:var(--black);font-size:40px;line-height:1;padding:14px 0 0 10px}
  .weight sup{font-size:18px;vertical-align:top;position:relative;top:-2px}
  .bottom-strip{position:absolute;left:0;top:720px;width:100%;height:15px;background:var(--yellow)}

  /* back */
  .back{left:467px;width:468px;background:var(--yellow)}
  .back .top-strip{position:absolute;left:0;top:0;width:468px;height:22px;background:var(--black)}
  .back .tab{left:108px;width:253px;background:var(--black);color:var(--yellow)}
  .section-tag{position:absolute;left:23px;height:17px;background:var(--black);color:var(--white);
    font-weight:700;font-size:10.5px;padding:2px 28px 0 5px;border-radius:0 3px 3px 0}
  .copy{position:absolute;left:23px;width:425px;font-size:10.7px;line-height:14.5px;color:var(--black);text-align:justify}
  .copy b{font-weight:700}
  .directions{position:absolute;left:23px;top:228px;width:425px;list-style:none;font-size:10.2px;line-height:14.5px;letter-spacing:-.15px}
  .directions li{padding-left:18px;position:relative}
  .directions li b{display:block;font-weight:700}
  .directions li::before{content:attr(data-n);position:absolute;left:0;font-weight:700}
  .extra{position:absolute;left:23px;top:436px;width:425px;font-size:9px;line-height:12px}
  .extra p{text-align:justify}
  .caution{position:absolute;left:23px;top:482px;font-size:9px;line-height:12px;font-weight:600}
  .caution span{color:var(--red);font-weight:600}
  .safety{position:absolute;left:0;top:520px;width:468px;height:139px;background:var(--white);border-top:6px solid var(--black)}
  .safety svg{position:absolute;left:8px;top:26px}
  .safety-text{position:absolute;left:97px;top:10px;width:350px;font-size:9px;line-height:12px;text-align:justify}
  .safety-text h3{font-size:9.5px;font-weight:700;margin-bottom:4px}
  .safety-text .warn{color:var(--red);font-weight:700}
  .safety-text .sds{font-weight:700;margin-top:6px}
  .footer{position:absolute;left:0;top:659px;width:468px;height:61px;background:var(--black);color:var(--white)}
  .footer-name{position:absolute;left:20px;top:22px;width:100px;font-weight:900;font-size:14px;color:var(--white);letter-spacing:.2px;white-space:nowrap}
  .footer-details{position:absolute;left:130px;top:14px;font-size:9.5px;line-height:13px;white-space:nowrap}
  .footer-details strong{color:var(--yellow);font-weight:700}
  .back .bottom-strip{background:var(--yellow)}
</style>
</head>
<body>
<div class="label">

  <section class="panel front">
    <div class="front-texture" role="img" aria-label="Dark hexagon texture background"></div>
    <div class="top-strip"></div>
    <div class="tab">PROFESSIONAL USE</div>

    <div class="brand">
      <div class="brand-name">DOVVRANTI</div>
      <div class="brand-tagline">PROFESSIONAL CLEANING | MAXIMUM PERFORMANCE</div>
    </div>

    <div class="product-name">INK PURGE</div>
    <div class="product-sub">ADVANCE ANILOX CLEANING GEL</div>

    <div class="claims">
      <div class="claim">
        <svg width="72" height="72" viewBox="0 0 72 72" role="img" aria-label="No caustic skull icon">
          <circle cx="36" cy="36" r="33" fill="none" stroke="var(--yellow)" stroke-width="4"/>
          <circle cx="36" cy="31" r="11" fill="var(--white)"/>
          <rect x="30" y="38" width="12" height="8" rx="2" fill="var(--white)"/>
          <circle cx="32" cy="30" r="3" fill="var(--black)"/><circle cx="40" cy="30" r="3" fill="var(--black)"/>
          <path d="M22 48 L50 58 M50 48 L22 58" stroke="var(--white)" stroke-width="3.5" stroke-linecap="round"/>
          <line x1="13" y1="13" x2="59" y2="59" stroke="var(--yellow)" stroke-width="4"/>
        </svg>NON<br>CAUSTIC
      </div>
      <div class="claim">
        <svg width="72" height="72" viewBox="0 0 72 72" role="img" aria-label="No toxic flask icon">
          <circle cx="36" cy="36" r="33" fill="none" stroke="var(--yellow)" stroke-width="4"/>
          <path d="M31 16 H41 V30 L52 54 H20 L31 30 Z" fill="none" stroke="var(--white)" stroke-width="3.5" stroke-linejoin="round"/>
          <path d="M25 46 H47 L51 54 H21 Z" fill="var(--white)"/>
          <line x1="13" y1="13" x2="59" y2="59" stroke="var(--yellow)" stroke-width="4"/>
        </svg>NON<br>TOXIC
      </div>
      <div class="claim">
        <svg width="72" height="72" viewBox="0 0 72 72" role="img" aria-label="No flammable flame icon">
          <circle cx="36" cy="36" r="33" fill="none" stroke="var(--yellow)" stroke-width="4"/>
          <path d="M36 14 C40 24 50 30 50 44 C50 53 44 58 36 58 C28 58 22 53 22 44 C22 36 28 32 30 24 C33 30 34 33 36 34 C38 28 38 22 36 14 Z" fill="var(--white)"/>
          <line x1="13" y1="13" x2="59" y2="59" stroke="var(--yellow)" stroke-width="4"/>
        </svg>NON<br>FLAMMABLE
      </div>
      <div class="claim">
        <svg width="72" height="72" viewBox="0 0 72 72" role="img" aria-label="No corrosive hand icon">
          <circle cx="36" cy="36" r="33" fill="none" stroke="var(--yellow)" stroke-width="4"/>
          <rect x="16" y="18" width="18" height="12" fill="none" stroke="var(--white)" stroke-width="3"/>
          <path d="M30 42 H50 C54 42 54 48 50 48 H30 Z" fill="var(--white)"/>
          <path d="M22 38 H32 V52 H22 Z" fill="var(--white)"/>
          <line x1="13" y1="13" x2="59" y2="59" stroke="var(--yellow)" stroke-width="4"/>
        </svg>NON<br>CORROSIVE
      </div>
    </div>

    <div class="suitable">SUITABLE<br><span>FOR</span></div>
    <div class="ink-badges">
      <div class="ink-badge blue"><svg width="18" height="24" viewBox="0 0 18 24"><path d="M9 1 C13 8 17 12 17 16 A8 8 0 0 1 1 16 C1 12 5 8 9 1 Z" fill="#fff"/></svg><em>UV BASED INK</em></div>
      <div class="ink-badge green"><svg width="18" height="24" viewBox="0 0 18 24"><path d="M9 1 C13 8 17 12 17 16 A8 8 0 0 1 1 16 C1 12 5 8 9 1 Z" fill="#fff"/></svg><em>UV BASED INK</em></div>
      <div class="ink-badge amber"><svg width="18" height="24" viewBox="0 0 18 24"><path d="M9 1 C13 8 17 12 17 16 A8 8 0 0 1 1 16 C1 12 5 8 9 1 Z" fill="#fff"/></svg><em>UV BASED INK</em></div>
    </div>

    <div class="weight">1<sup>KG</sup></div>
    <div class="bottom-strip"></div>
  </section>

  <section class="panel back">
    <div class="top-strip"></div>
    <div class="tab">PROFESSIONAL USE</div>

    <div class="section-tag" style="top:60px">Uses :</div>
    <div class="copy" style="top:83px">
      <p><b>INK PURGE</b> is a highly concentrated, powerful cleaning gel formulated to safely remove solvent-based, water-based, and UV inks from anilox rollers.</p>
      <p>It’s thickened formula clings to surfaces, allowing deep penetration into anilox cells and is safe for use on both ceramic and chrome rollers.</p>
      <p><b>INK PURGE</b> Gel is also suitable for general pressroom cleaning of machinery, components and floors.</p>
      <p><b>Additionally,</b> it can be used to remove most varnishes, coatings, and emulsion adhesives.</p>
    </div>

    <div class="section-tag" style="top:206px">Directions:</div>
    <ol class="directions">
      <li data-n="1."><b>Apply:</b>Apply INK PURGE Gel directly to the surface of the anilox roller using an anilox cleaning pad or brush. Ensure full and even coverage with a thick layer of gel.</li>
      <li data-n="2."><b>Dwell Time:</b>Allow the gel to sit for 10–15 minutes</li>
      <li data-n="3."><b>Agitate :</b>Use a anilox cleaning pad or brush to agitate and remove stubborn ink deposits.</li>
      <li data-n="4."><b>Rinse Thoroughly:</b>Rinse the roller thoroughly with warm water to remove all residue.</li>
      <li data-n="5."><b>Dry:</b>Wipe dry with a clean lint-free cloth making sure the roller is completely dry before returning to production.</li>
    </ol>

    <div class="extra">
      <p><b>INK PURGE</b> Gel can also be used for general press cleaning (rubber rollers, ink trays, doctor blades, press room floors etc)</p>
      <p><b>For more information see full product data sheet</b></p>
    </div>
    <div class="caution"><span>CAUTION</span><br>pre testing on all surfaces is recommended before use.</div>

    <div class="safety">
      <svg width="84" height="84" viewBox="0 0 84 84" role="img" aria-label="Exclamation hazard pictogram">
        <rect x="17" y="17" width="50" height="50" transform="rotate(45 42 42)" fill="var(--white)" stroke="var(--red)" stroke-width="6"/>
        <rect x="38" y="22" width="8" height="28" rx="4" fill="var(--black)"/>
        <circle cx="42" cy="59" r="5" fill="var(--black)"/>
      </svg>
      <div class="safety-text">
        <h3>Health and Safety</h3>
        <p>Contains - &lt;5% Non-Ionic surfactants</p>
        <p><span class="warn">WARNING</span> Contains: Alcohols, C9-11, ethoxylated. Causes skin irritation. Causes serious eye irritation. Wash hands thoroughly after handling. Wear eye protection. <span class="warn">IF IN EYES:</span> Rinse cautiously with water for several minutes. Remove contact lenses, if present and easy to do. Continue rinsing. If eye irritation persists: Get medical advice/attention.</p>
        <p class="sds">See SDS for full safety information</p>
      </div>
    </div>

    <div class="footer">
      <div class="footer-name">DOVVRANTI</div>
      <div class="footer-details">
        <strong>DOVVRANTI LTD</strong><br>
        48 Fernhill Road, Dunmore, DN4 7QT<br>
        ✉ info@dovvranti.co.uk | ⊕ www.dovvranti.co.uk
      </div>
    </div>
    <div class="bottom-strip"></div>
  </section>

</div>
</body>
</html>
```